New Zealand Luggage Importer Needs Business Cards

We need professional, creative and fashionable business cards created.
We are based in New Zealand and import and distribute high-end, quality, fashionable and durable luggage.
We pride ourselves on selling the very best quality luggage, second only to 1 brand (which we won't mention here)...we use the same manufacturer. However, our prices are much more reasonable.
Industry/Entity Type
Business
Contact Information for Business Card
Mark Dunsley
027 512 4068
3/17 Harlow Street, Pinecrest Flats, Auckland, 0614
PO Box 204377, Fernside, Auckland 0731
09-528-3916
sales@brivancases.co.nz / www.brivancases.co.nz

```html
<!DOCTYPE html>
<html lang="en">
<head>
<meta charset="utf-8">
<title>Brivan Cases – Business Card</title>
<link rel="stylesheet" href="https://fonts.googleapis.com/css2?family=Open+Sans:wght@400;600;700&display=swap">
<style>
  :root {
    --bg: #e6e7ea;
    --card: #f6f6f7;
    --card-edge: #d9dadd;
    --ink-strong: #3b3c3f;
    --ink: #5b5c60;
    --ink-soft: #6a6b70;
    --gold: #b39a4c;
    --gold-light: #e9dc9c;
    --gold-deep: #cdb968;
  }
  * { box-sizing: border-box; margin: 0; padding: 0; }
  html, body {
    width: 1200px;
    height: 970px;
    overflow: hidden;
    background: var(--bg);
    font-family: "Open Sans", Arial, sans-serif;
  }
  .canvas {
    width: 1200px;
    height: 970px;
    display: flex;
    align-items: center;
    justify-content: center;
  }
  .card {
    position: relative;
    width: 1000px;
    height: 568px;
    background: var(--card);
    border: 1px solid var(--card-edge);
    border-radius: 26px;
    overflow: hidden;
    box-shadow: 0 10px 30px rgba(0, 0, 0, 0.08);
  }
  .brand {
    position: absolute;
    left: 28px;
    top: 22px;
    font-size: 58px;
    font-weight: 700;
    letter-spacing: 1px;
    color: var(--ink-strong);
    line-height: 1;
  }
  .person {
    position: absolute;
    left: 38px;
    top: 150px;
    font-size: 36px;
    font-weight: 600;
    color: var(--ink-soft);
  }
  .contacts {
    position: absolute;
    left: 38px;
    top: 222px;
    list-style: none;
  }
  .contact {
    display: flex;
    align-items: center;
    height: 46px;
    font-size: 23px;
    color: var(--ink);
  }
  .contact-icon {
    width: 26px;
    height: 26px;
    margin-right: 23px;
    flex: none;
    fill: var(--gold);
  }
  .contact-text--indent { margin-left: 49px; }
  .gold-band {
    position: absolute;
    left: 0;
    right: 0;
    bottom: 0;
    height: 48px;
    background: linear-gradient(180deg, var(--gold-light), var(--gold-deep));
  }
</style>
</head>
<body>
<main class="canvas">
  <section class="card" aria-label="Business card">
    <div class="brand">BRIVAN CASES</div>
    <h1 class="person">Mark Dunsley</h1>
    <ul class="contacts">
      <li class="contact">
        <svg class="contact-icon" viewBox="0 0 24 24" aria-hidden="true"><path d="M7 1h10a2 2 0 0 1 2 2v18a2 2 0 0 1-2 2H7a2 2 0 0 1-2-2V3a2 2 0 0 1 2-2zm0 3v14h10V4zm5 15.5a1.2 1.2 0 1 0 0 2.4 1.2 1.2 0 0 0 0-2.4z"/></svg>
        <span class="contact-text">027 512 4068</span>
      </li>
      <li class="contact">
        <svg class="contact-icon" viewBox="0 0 24 24" aria-hidden="true"><path d="M2 8c0-2 4-4 10-4s10 2 10 4v2h-5V8H7v2H2zm4 4h12l3 8H3zm6 1.5a3 3 0 1 0 0 6 3 3 0 0 0 0-6z"/></svg>
        <span class="contact-text">09-528-3916</span>
      </li>
      <li class="contact">
        <svg class="contact-icon" viewBox="0 0 24 24" aria-hidden="true"><path d="M2 5h20v14H2zm2 2v.5l8 5.5 8-5.5V7zm0 3v7h16v-7l-8 5.5z"/></svg>
        <span class="contact-text">sales@brivancases.co.nz</span>
      </li>
      <li class="contact">
        <svg class="contact-icon" viewBox="0 0 24 24" aria-hidden="true"><path d="M12 2a10 10 0 1 0 0 20 10 10 0 0 0 0-20zm0 2c1 0 2.3 2 2.8 5H9.2C9.7 6 11 4 12 4zM4.3 11h3a17 17 0 0 0 0 2h-3a8 8 0 0 1 0-2zm4.9 0h5.6a15 15 0 0 1 0 2H9.2a15 15 0 0 1 0-2zm7.5 0h3a8 8 0 0 1 0 2h-3a17 17 0 0 0 0-2zM9.2 15h5.6c-.5 3-1.8 5-2.8 5s-2.3-2-2.8-5z"/></svg>
        <span class="contact-text">www.brivancases.co.nz</span>
      </li>
      <li class="contact">
        <svg class="contact-icon" viewBox="0 0 24 24" aria-hidden="true"><path d="M12 1a7 7 0 0 0-7 7c0 5 7 15 7 15s7-10 7-15a7 7 0 0 0-7-7zm0 4a3 3 0 1 1 0 6 3 3 0 0 1 0-6z"/></svg>
        <span class="contact-text">3/17 Harlow Street, Pinecrest Flats, Auckland, 0614</span>
      </li>
      <li class="contact">
        <span class="contact-text contact-text--indent">PO Box 204377, Fernside, Auckland 0731</span>
      </li>
    </ul>
    <div class="gold-band"></div>
  </section>
</main>
</body>
</html>
```